Business card for Northland's Blue Wagon.

Good day i am looking for a business card design for my business.
The name of the business is Northland's Blue Wagon. It is a van rental business that provides a driver and helper to the customer. Customer have use to van for small moves, studio or 1 bedroom, Moving furniture like couch or kitchen cabinets.
We are available evenings, weekends and holidays.
the means to contact us is by phone at 628-947-2071; By emails at Oakridge@northlandsbluewagon.net; or by social media, Facebook and Instagram.
You can see attached pictures of the van and or logo.

```html
<!DOCTYPE html>
<html lang="en">
<head>
<meta charset="utf-8">
<title>Northland's Blue Wagon — Business Card</title>
<link rel="stylesheet" href="https://fonts.googleapis.com/css2?family=Montserrat:wght@400;500;700;800&display=swap">
<style>
  :root {
    --canvas: #e6e4e2;
    --card-white: #ffffff;
    --card-black: #161616;
    --brand-red: #d71920;
    --ink: #1d1d1d;
    --shadow: rgba(0,0,0,0.18);
  }
  * { box-sizing: border-box; margin: 0; padding: 0; }
  html, body {
    width: 1200px; height: 786px; overflow: hidden;
    background: var(--canvas);
    font-family: "Montserrat", Arial, sans-serif;
  }
  .stage {
    position: relative; width: 1200px; height: 786px;
    display: flex; align-items: center; justify-content: center; gap: 40px;
  }
  .card {
    position: relative; width: 560px; height: 320px;
    box-shadow: 0 10px 28px var(--shadow);
  }
  .card--front { background: var(--card-white); color: var(--ink); }
  .card--back { background: var(--card-black); }

  .brand-mark {
    position: absolute; display: flex; align-items: center; gap: 12px;
    color: var(--brand-red); font-weight: 700; font-size: 19px; letter-spacing: 0.5px;
  }
  .brand-mark__dot { width: 40px; height: 40px; border-radius: 50%; background: var(--brand-red); flex: none; }
  .card--front .brand-mark { top: 70px; right: 48px; }
  .card--back .brand-mark { top: 50%; left: 50%; transform: translate(-50%, -50%); font-size: 24px; }
  .card--back .brand-mark__dot { width: 48px; height: 48px; }

  .rule-long { position: absolute; top: 152px; left: 150px; right: 40px; height: 1.5px; background: var(--brand-red); }
  .rule-short { position: absolute; top: 203px; left: 34px; width: 170px; height: 1.5px; background: var(--brand-red); }

  .person { position: absolute; left: 34px; top: 158px; }
  .person__name { color: var(--brand-red); font-weight: 800; font-size: 23px; letter-spacing: 0.3px; line-height: 1.1; }
  .person__title { font-weight: 500; font-size: 13px; letter-spacing: 0.6px; margin-top: 2px; }

  .contacts { position: absolute; left: 34px; top: 214px; list-style: none; }
  .contacts li { display: flex; align-items: center; gap: 10px; font-size: 12.5px; font-weight: 500; height: 23px; }
  .contacts svg { width: 14px; height: 14px; flex: none; }
  .contacts .plain-square { width: 13px; height: 13px; border-radius: 3px; background: var(--brand-red); flex: none; }

  .address { position: absolute; right: 40px; top: 172px; text-align: right; font-size: 12.5px; line-height: 1.45; font-weight: 500; }
</style>
</head>
<body>
<main class="stage">
  <section class="card card--front" aria-label="Business card front">
    <div class="brand-mark"><span class="brand-mark__dot"></span><span>Northland's Blue Wagon</span></div>
    <div class="rule-long"></div>
    <div class="person">
      <p class="person__name">Renaud Tremblay</p>
      <p class="person__title">Managing Director</p>
    </div>
    <div class="rule-short"></div>
    <ul class="contacts">
      <li>
        <svg viewBox="0 0 24 24" aria-hidden="true"><path fill="var(--brand-red)" d="M6.6 10.8a15.1 15.1 0 0 0 6.6 6.6l2.2-2.2c.3-.3.7-.4 1-.2 1.1.4 2.3.6 3.6.6.6 0 1 .4 1 1V20c0 .6-.4 1-1 1A17 17 0 0 1 3 4c0-.6.4-1 1-1h3.5c.6 0 1 .4 1 1 0 1.3.2 2.5.6 3.6.1.3 0 .7-.2 1z"/></svg>
        <span>628-947-2071</span>
      </li>
      <li>
        <svg viewBox="0 0 24 24" aria-hidden="true"><rect x="2" y="5" width="20" height="14" rx="1.5" fill="var(--brand-red)"/><path d="M3 6l9 7 9-7" fill="none" stroke="#fff" stroke-width="1.6"/></svg>
        <span>Oakridge@northlandsbluewagon.net</span>
      </li>
      <li><span class="plain-square"></span><span>northlandsbluewagon.net</span></li>
      <li><span class="plain-square"></span><span>@northlandsbluewagon</span></li>
    </ul>
    <p class="address">248 Cedar Hollow Road<br>Brandon, MS 39047</p>
  </section>

  <section class="card card--back" aria-label="Business card back">
    <div class="brand-mark"><span class="brand-mark__dot"></span><span>Northland's Blue Wagon</span></div>
  </section>
</main>
</body>
</html>
```